Korlane Email Signature Banners – Fabrication Capability Series

www.Korlane.com.au is an Australian engineering and fabrication company specialising in fabrication and welding of :
steel piping spools,
skids and frames,
small volume process steel tanks
and general steel fabrication
We require four distinct banner designs for use in Velnor Tidmark email signatures. Each banner will highlight a specific capability while maintaining a consistent brand identity.
Deliverables
Four banners total:
Piping Spools Fabrication – focus on precision welding and stainless steel pipework
Skid & Frames Fabrication – highlight skid systems and structural frames
Small Steel Tanks Fabrication – show fabricated tanks and workshop craftsmanship
General Fabrication Solutions – broad steel fabrication theme for company-wide use
Dimensions: 600–700 px wide × 100 px high
Format: PNG (preferred), small file size prefered
Resolution: 72 dpi
Background: non-transparent, industrial or workshop setting
Text examples:
1. Piping Spools Fabrication
Option A: “Expert Fabrication Solutions for Process Piping”
Option B: “Precision Welding for Complex Systems”
Option C: “Delivering Quality in Every Spool”
Option D: “Engineered for Flow, Built for Strength”
2. Skid & Frames Fabrication
Option A: “Custom Engineered Modular Systems”
Option B: “Built Strong. Designed Smart.”
Option C: “Reliable Frames for Industrial Performance”
Option D: “Modular Fabrication for Seamless Integration”
3. Small Steel Tanks Fabrication
Option A: “Precision Built for Your Needs”
Option B: “Compact Strength. Proven Durability.”
Option C: “Fabricated for Performance and Longevity”
Option D: “Small Tanks. Big Reliability.”
4. General Fabrication Solutions
Option A: “Quality Craftsmanship, Proven Results”
Option B: “Your Partner in Precision Fabrication”
Option C: “Engineering Excellence in Every Weld”
Option D: “Australian Fabrication. Global Standards.”
Style Direction
Clean, professional, and engineering‑focused
Use Korlane brand colours
Blend photo realism with vector clarity (no heavy gradients)
Include subtle industrial textures or workshop imagery
Typography: bold sans‑serif, legible at small scale
Usage Context
These banners will appear at the bottom of staff email signatures via Tidmark Email Signature Tool for Velnor 365, so clarity and fast loading are essential. No Logo is required in the banners.
Reference
Existing Korlane signature is attached. Colour palette to match the signature style and logo.
Target Market(s)
Engineering and construction companies,
Industry/Entity Type
Engineering fabrication design
Look and feel

```html
<!DOCTYPE html>
<html lang="en">
<head>
<meta charset="utf-8">
<title>Korlane Signature Banners – Piping Spools Fabrication, Option C</title>
<link rel="stylesheet" href="https://fonts.googleapis.com/css2?family=Outfit:wght@600;700&display=swap">
<style>
  :root {
    --page-bg: #ffffff;
    --ink: #0b0b0b;
    --brand-blue: #1eaae2;
    --brand-grey: #96979b;
    --banner-text: #ffffff;
    --photo-dark: #3a3733;
    --photo-mid: #6b6660;
    --photo-steel: #8d8c88;
    --photo-blue: #3d5a78;
  }
  * { box-sizing: border-box; margin: 0; padding: 0; }
  html, body {
    width: 1200px;
    height: 1106px;
    overflow: hidden;
    background: var(--page-bg);
  }
  body {
    position: relative;
    font-family: "Outfit", "Helvetica Neue", Arial, sans-serif;
    color: var(--ink);
  }
  .sheet-title {
    position: absolute;
    left: 78px;
    top: 148px;
    font-size: 25px;
    font-weight: 700;
    line-height: 31px;
    letter-spacing: -0.2px;
  }
  .banner {
    position: absolute;
    left: 251px;
    width: 702px;
    height: 100px;
    overflow: hidden;
  }
  .banner--stacked { display: flex; flex-direction: column; }
  .banner--stacked .banner__photo { height: 60px; width: 100%; }
  .banner--stacked .banner__band {
    height: 40px;
    display: flex;
    align-items: center;
    justify-content: center;
    font-size: 24px;
  }
  .banner--split { display: flex; }
  .banner--split .banner__band {
    width: 330px;
    height: 100%;
    padding-left: 28px;
    display: flex;
    align-items: center;
    font-size: 26.5px;
    line-height: 32px;
  }
  .banner--split .banner__photo { flex: 1; height: 100%; }
  .banner__band {
    color: var(--banner-text);
    font-weight: 700;
    letter-spacing: 0.1px;
  }
  .banner__band--blue { background: var(--brand-blue); }
  .banner__band--grey { background: var(--brand-grey); }
  .banner__photo {
    background:
      linear-gradient(90deg, rgba(61,90,120,0) 70%, rgba(61,90,120,0.45) 88%, rgba(58,55,51,0.3) 100%),
      linear-gradient(180deg, var(--photo-steel) 0%, var(--photo-mid) 45%, var(--photo-dark) 100%);
  }
  .banner-one   { top: 284px; }
  .banner-two   { top: 472px; }
  .banner-three { top: 664px; }
  .banner-four  { top: 851px; }
  .page-number {
    position: absolute;
    right: 22px;
    top: 1077px;
    font-size: 11px;
    font-weight: 600;
  }
</style>
</head>
<body>
  <h1 class="sheet-title">1. Piping Spools Fabrication<br>Option C: “Delivering Quality in Every Spool”</h1>

  <section class="banner banner--stacked banner-one">
    <div class="banner__photo" role="img" aria-label="Workshop photo: welder joining a stainless steel pipe spool beside an inspector with a clipboard"></div>
    <div class="banner__band banner__band--blue">Delivering Quality in Every Spool</div>
  </section>

  <section class="banner banner--split banner-two">
    <div class="banner__band banner__band--blue">Delivering Quality in<br>Every Spool</div>
    <div class="banner__photo" role="img" aria-label="Workshop photo: welder fabricating a flanged stainless steel pipe spool with finished spools on racks"></div>
  </section>

  <section class="banner banner--stacked banner-three">
    <div class="banner__photo" role="img" aria-label="Workshop photo: welder joining a stainless steel pipe spool beside an inspector with a clipboard"></div>
    <div class="banner__band banner__band--grey">Delivering Quality in Every Spool</div>
  </section>

  <section class="banner banner--split banner-four">
    <div class="banner__band banner__band--grey">Delivering Quality in<br>Every Spool</div>
    <div class="banner__photo" role="img" aria-label="Workshop photo: welder fabricating a flanged stainless steel pipe spool with finished spools on racks"></div>
  </section>

  <div class="page-number">005</div>
</body>
</html>
```